Business Cards used to invite people to our church

We are a church and have need of a business card sized advertisement that allows our members to hand them out in order to invite people to the church. I need the front of the card to say "You're Invited" or "Come Check us out". with the service times on the back of the card later.
I have attached one of the OLD cards we have used in the past, but we want a complete makeover, into a more modern style that does not require the image.
I am also replacing the old logo with a newer "flat" logo which is attached.
Please use marketing colors. (blue or red or something that catches attention)
Create a card that DOES NOT have the picture of the two people on the front
The information on the sample card back is correct to go onto new card
Target Market(s)
anyone
Industry/Entity Type
Business
Contact Information for Business Card
sertice times and address information which you can get from the sample card I uploaded. It should have "You're Invited" or "Come Check us out" on the front of the card with out logo.
Look and feel
Each slider illustrates characteristics of the customer's brand and the style your logo design should communicate.

```html
<!DOCTYPE html>
<html lang="en">
<head>
<meta charset="utf-8">
<title>Harbor Light – Invitation Card</title>
<link href="https://fonts.googleapis.com/css2?family=Dancing+Script:wght@500&family=Jost:wght@400;600&display=swap" rel="stylesheet">
<style>
  :root{
    --stage:#1b1b1b;
    --blue-deep:#0a5cff;
    --blue-mid:#0a86f0;
    --blue-edge:#138fd6;
    --cyan-glow:#00f2ff;
    --pink:#f79bca;
    --white:#ffffff;
  }
  *{margin:0;padding:0;box-sizing:border-box}
  html,body{width:981px;height:1200px;overflow:hidden;background:var(--stage)}
  .canvas{position:relative;width:981px;height:1200px}
  .card{
    position:absolute;left:75px;width:831px;height:486px;overflow:hidden;
    background:
      radial-gradient(circle at 34% 30%, var(--cyan-glow) 0%, #08b8ff 18%, var(--blue-deep) 55%, var(--blue-mid) 80%, var(--blue-edge) 100%);
  }
  .card--front{top:75px}
  .card--back{top:638px}
  .card__sweep{position:absolute;inset:0;width:831px;height:486px}

  /* front */
  .brand-mark{
    position:absolute;left:200px;top:100px;width:440px;
    font-family:'Jost',sans-serif;font-weight:600;color:var(--pink);
    font-size:88px;line-height:180px;text-align:center;letter-spacing:2px;
  }
  .invite-band{
    position:absolute;left:0;top:197px;width:831px;height:93px;
    background:linear-gradient(90deg, rgba(255,255,255,.85) 0%, rgba(255,255,255,.35) 12%, rgba(255,255,255,.3) 75%, rgba(255,255,255,.55) 92%, rgba(255,255,255,.95) 100%);
  }
  .invite-text{
    position:absolute;left:0;top:197px;width:831px;height:93px;
    font-family:'Dancing Script',cursive;font-weight:500;font-size:70px;color:var(--white);
    text-align:center;line-height:90px;padding-left:30px;
  }

  /* back */
  .contact{
    position:absolute;left:50px;top:78px;width:730px;text-align:center;
    font-family:'Jost',sans-serif;font-weight:400;color:var(--white);
    font-size:30px;line-height:40px;letter-spacing:.5px;
  }
  .divider-band{
    position:absolute;left:0;top:235px;width:831px;height:18px;
    background:linear-gradient(90deg, rgba(255,255,255,.95) 0%, rgba(255,255,255,.45) 15%, rgba(255,255,255,.35) 70%, rgba(255,255,255,.95) 100%);
  }
  .schedule{
    position:absolute;left:85px;top:328px;width:464px;list-style:none;
    font-family:'Jost',sans-serif;font-size:20px;line-height:27.5px;color:var(--white);
  }
  .schedule li{display:flex;align-items:baseline}
  .schedule .leader{flex:1;border-bottom:2px dotted var(--white);margin:0 2px 5px;opacity:.95}
  .back-brand{
    position:absolute;left:600px;top:330px;width:150px;text-align:right;
    font-family:'Jost',sans-serif;font-weight:600;font-size:26px;line-height:30px;color:var(--pink);
  }
</style>
</head>
<body>
<main class="canvas">

  <section class="card card--front" aria-label="Card front">
    <svg class="card__sweep" viewBox="0 0 831 486" aria-hidden="true">
      <path d="M554 0 C640 180 540 390 302 486 L831 486 L831 0 Z" fill="rgba(255,255,255,0.2)"/>
    </svg>
    <div class="brand-mark">HARBOR<br>LIGHT</div>
    <div class="invite-band"></div>
    <h1 class="invite-text">Come Check us out</h1>
  </section>

  <section class="card card--back" aria-label="Card back">
    <svg class="card__sweep" viewBox="0 0 831 486" aria-hidden="true">
      <defs>
        <clipPath id="left-of-sweep">
          <path d="M0 0 L554 0 C640 180 540 390 302 486 L0 486 Z"/>
        </clipPath>
      </defs>
      <path d="M554 0 C640 180 540 390 302 486 L831 486 L831 0 Z" fill="rgba(255,255,255,0.18)"/>
      <rect x="50" y="51" width="730" height="387" rx="18" fill="rgba(255,255,255,0.14)"/>
      <rect x="50" y="51" width="730" height="387" rx="18" fill="#f79bca" clip-path="url(#left-of-sweep)"/>
    </svg>

    <address class="contact">
      HARBORLIGHTCHURCH.ORG<br>
      482 W. CEDAR LANE-FAIRVIEW, TX 75990<br>
      1-800-555-0142
    </address>

    <div class="divider-band"></div>

    <ul class="schedule">
      <li><span>SUNDAY</span><span class="leader"></span><span>9:00 AM</span></li>
      <li><span>SUNDAY</span><span class="leader"></span><span>11:00 AM</span></li>
      <li><span>Wed. Bible Class</span><span class="leader"></span><span>7:00 PM</span></li>
    </ul>

    <div class="back-brand">HARBOR<br>LIGHT</div>
  </section>

</main>
</body>
</html>
```